Commercial facility maintenance

I need a card design that helps my salesmen make contact with new clients, our product is facility maintenance and heavy industrial maintenance

```html
<!DOCTYPE html>
<html lang="en">
<head>
<meta charset="utf-8">
<title>Brennan Industrial LLC – Business Card</title>
<link rel="stylesheet" href="https://fonts.googleapis.com/css2?family=Montserrat:wght@400;500;700;800&display=swap">
<style>
  :root {
    --page-bg: #d9d2c8;
    --card-bg: #ede8e0;
    --ink: #2f3033;
    --ink-soft: #3d3e42;
    --brand-red: #a3181f;
    --brand-red-deep: #861218;
    --swoosh: #3a3b3f;
    --badge-fill: #f6f3ee;
  }
  * { box-sizing: border-box; margin: 0; padding: 0; }
  html, body {
    width: 1200px; height: 1047px; overflow: hidden;
    background: var(--page-bg);
    font-family: "Montserrat", sans-serif;
    color: var(--ink);
  }
  .business-card {
    position: absolute; left: 125px; top: 263px;
    width: 950px; height: 520px;
    border-radius: 16px; overflow: hidden;
    background: var(--card-bg);
    box-shadow: 0 6px 24px rgba(0,0,0,.12);
  }
  .card-art { position: absolute; inset: 0; width: 950px; height: 520px; }
  .company-mark {
    position: absolute; left: 40px; top: 52px;
    display: flex; align-items: center; gap: 14px;
  }
  .company-mark__dot {
    width: 58px; height: 58px; border-radius: 50%;
    background: var(--ink);
  }
  .company-mark__name {
    font-weight: 800; font-size: 32px; letter-spacing: .5px;
    color: var(--ink); line-height: 1;
  }
  .person {
    position: absolute; right: 32px; top: 52px; text-align: right;
  }
  .person__name {
    font-weight: 700; font-size: 35px; letter-spacing: 1px; color: var(--ink);
  }
  .person__role {
    margin-top: 10px; font-weight: 500; font-size: 20px; color: var(--brand-red);
  }
  .address {
    position: absolute; left: 37px; top: 196px;
    font-size: 21px; line-height: 34px; color: var(--ink-soft);
  }
  .contact-list {
    position: absolute; left: 36px; top: 305px; list-style: none;
  }
  .contact-list li {
    display: flex; align-items: center; gap: 10px;
    font-size: 21px; height: 34px; color: var(--ink-soft);
  }
  .contact-list svg { width: 18px; height: 18px; fill: var(--brand-red); flex: none; }
  .badge-name {
    position: absolute; left: 631px; top: 270px; width: 260px;
    text-align: center; font-weight: 800; font-size: 27px; line-height: 36px;
    color: var(--ink);
  }
</style>
</head>
<body>
<main class="business-card">
  <svg class="card-art" viewBox="0 0 950 520" aria-hidden="true">
    <path d="M0 462 C 180 470, 330 490, 470 484 C 600 478, 680 430, 760 418 C 840 408, 900 418, 950 424 L950 520 L0 520 Z" fill="var(--brand-red)"/>
    <path d="M0 492 C 300 512, 650 500, 950 470 L950 520 L0 520 Z" fill="var(--brand-red-deep)" opacity=".45"/>
    <path d="M0 404 C 120 430, 260 470, 480 467 C 300 478, 140 462, 0 436 Z" fill="var(--swoosh)"/>
    <circle cx="761" cy="315" r="151" fill="var(--badge-fill)" stroke="var(--ink)" stroke-width="4"/>
  </svg>

  <div class="company-mark">
    <span class="company-mark__dot"></span>
    <span class="company-mark__name">BRENNAN INDUSTRIAL LLC</span>
  </div>

  <div class="person">
    <h1 class="person__name">DANIEL MOORE</h1>
    <p class="person__role">Managing Director</p>
  </div>

  <address class="address" style="font-style:normal">
    Your address, City<br>State, Zip 1234
  </address>

  <ul class="contact-list">
    <li><svg viewBox="0 0 24 24"><path d="M6.6 10.8a15 15 0 0 0 6.6 6.6l2.2-2.2a1 1 0 0 1 1-.25 11.4 11.4 0 0 0 3.6.57 1 1 0 0 1 1 1V20a1 1 0 0 1-1 1A17 17 0 0 1 3 4a1 1 0 0 1 1-1h3.5a1 1 0 0 1 1 1c0 1.25.2 2.45.57 3.57a1 1 0 0 1-.25 1z"/></svg>555-014-2278</li>
    <li><svg viewBox="0 0 24 24"><path d="M2 5h20v14H2z M2 5l10 8 10-8" /></svg>info@brennanindustrialllc.com</li>
    <li><svg viewBox="0 0 24 24"><path d="M12 2a10 10 0 1 0 0 20 10 10 0 0 0 0-20zm0 2c1 1.3 1.8 3.2 2.1 5H9.9C10.2 7.2 11 5.3 12 4zM4.3 13a8 8 0 0 1 0-2h3.6a17 17 0 0 0 0 2zm5.6 0a15 15 0 0 1 0-2h4.2a15 15 0 0 1 0 2zm6.2 0a17 17 0 0 0 0-2h3.6a8 8 0 0 1 0 2zM12 20c-1-1.3-1.8-3.2-2.1-5h4.2c-.3 1.8-1.1 3.7-2.1 5z"/></svg>brennanindustrialllc.com</li>
  </ul>

  <p class="badge-name">BRENNAN<br>INDUSTRIAL<br>LLC</p>
</main>
</body>
</html>
```